Corporate Wall Mural for Office

We have several offices across North America and we want to have a corporate wall mural in each office, so we require a mural wall design that can be adjusted for different wall dimensions and still look good.

The first mural will be 239.5" x 112.5" it will be in our Toronto office - so the background city will be the Toronto skyline

I have attached a draft design and the content PNG file.

We want a different design that keeps the content outlined in the Mural Design Content PNG file.

Our corporate font is Gilroy Semi Bold

Our corporate colors are
Blue
C94
M70
Y0
K12
Pantone 2945C

Purple
C 80
M 78
PMS 2368 C

Sky Blue
C68
M34
PMS 2727 C
Our website is qalverpoint.com

Founded in 2012, QPT is a leading provider of technology infrastructure solutions, specializing in Broadband, DAS/Private Networks, Fixed Wireless Access, Site Solutions, Carrier Networks, and Test & Measurement. Our mission is to empower organizations of all sizes with innovative connectivity and telecom infrastructure solutions to build the future of communications.

Target Market(s)

Target is the staff and visitors of our office

Industry/Entity Type

network infrastructure: both wireless and wireline

Font styles to use
Sans Serif
Other font styles liked:
• Gilroy Semi-Bold and Bold

Colors
0054AA
0677BA
7BADD7
CADEEF
E8F1F8

Requirements
Must have
• the info listed in the Mural Content.png file, our corporate colors. It should be bright and energetic.
Nice to have
• I like concept of the city silhouette from the draft design

```html
<!DOCTYPE html>
<html lang="en">
<head>
<meta charset="utf-8">
<title>QPT Office Mural</title>
<link href="https://fonts.googleapis.com/css2?family=Outfit:wght@400;500;600;700;800&display=swap" rel="stylesheet">
<style>
  :root{
    --navy:#0b2f6b;
    --blue:#0054aa;
    --mid-blue:#0677ba;
    --sky:#4a92d3;
    --pale:#cadeef;
    --mist:#e8f1f8;
    --purple:#4b4fa8;
    --ink:#0d1424;
    --black:#050608;
    --white:#ffffff;
  }
  *{margin:0;padding:0;box-sizing:border-box}
  html,body{width:1200px;height:564px;overflow:hidden;background:var(--white)}
  body{font-family:"Outfit",sans-serif;color:var(--white)}
  .mural{position:relative;width:1200px;height:564px}
  .backdrop{position:absolute;inset:0}
  .abs{position:absolute}

  .brand{left:72px;top:80px;display:flex;align-items:center;gap:16px}
  .brand-dot{width:60px;height:60px;border-radius:50%;background:var(--blue)}
  .brand-name{font-size:58px;font-weight:700;color:var(--ink);letter-spacing:1px;line-height:1}

  .headline{left:480px;top:60px;width:670px;text-align:center;font-size:29px;font-weight:600;color:var(--white);letter-spacing:.2px}
  .subline{left:470px;top:108px;width:680px;text-align:center;font-size:19.5px;font-weight:500;color:var(--ink)}

  .unique{left:78px;top:172px;width:300px}
  .unique h2{font-size:17px;font-weight:700;color:var(--sky);margin-bottom:7px}
  .unique p{font-size:13px;line-height:16.5px;margin-bottom:4px;font-weight:400}
  .unique b{font-weight:700}

  .values-title{left:78px;top:309px;font-size:19px;font-weight:700;color:var(--sky)}

  .pill{position:absolute;height:31px;border-radius:16px;background:linear-gradient(180deg,#ffffff,#dce9f5);display:flex;align-items:center;box-shadow:0 2px 4px rgba(0,0,0,.3)}
  .pill-icon{width:34px;height:34px;margin-left:-2px;border-radius:50%;background:var(--white);border:3px solid var(--blue);flex:none;display:flex;align-items:center;justify-content:center}
  .pill-label{font-size:11.5px;font-weight:700;font-style:italic;color:var(--blue);line-height:11.5px;padding-left:10px}

  .card{position:absolute;background:var(--white);border-radius:14px;box-shadow:0 4px 10px rgba(0,0,0,.35)}
  .card-frame{position:absolute;inset:5px 6px 8px 6px;border:3px solid var(--blue);border-radius:10px;overflow:hidden;background:var(--white);z-index:1}
  .card-tab{position:absolute;top:-12px;left:22px;width:108px;height:33px;z-index:2}
  .card-tab span{position:absolute;inset:0;display:flex;align-items:center;justify-content:center;text-align:center;font-size:12px;font-weight:700;line-height:12.5px;color:var(--white)}
  .card ul{list-style:none;position:absolute;left:11px;top:20px;right:4px}
  .card li{position:relative;font-size:10.3px;line-height:14px;color:var(--ink);padding-left:9px}
  .card li::before{content:"";position:absolute;left:0;top:5px;width:4px;height:4px;border:1.2px solid var(--blue);border-radius:50%}
  .card-photo{position:absolute;left:0;right:0;bottom:0}

  .url{left:825px;top:483px;width:270px;text-align:center;font-size:21px;font-weight:600;color:var(--white);letter-spacing:.3px}
</style>
</head>
<body>
<div class="mural">
  <svg class="backdrop" width="1200" height="564" viewBox="0 0 1200 564" aria-hidden="true">
    <defs>
      <linearGradient id="panelBlue" x1="0" y1="0" x2="1" y2="1">
        <stop offset="0" stop-color="#0e3f86"/>
        <stop offset=".55" stop-color="#0a2f6a"/>
        <stop offset="1" stop-color="#1c72c4"/>
      </linearGradient>
      <linearGradient id="rightBlue" x1="0" y1="0" x2="0" y2="1">
        <stop offset="0" stop-color="#1a6fc2"/>
        <stop offset="1" stop-color="#0c3f8c"/>
      </linearGradient>
      <linearGradient id="city" x1="0" y1="0" x2="0" y2="1">
        <stop offset="0" stop-color="#ffffff"/>
        <stop offset=".35" stop-color="#e9ebee"/>
        <stop offset=".7" stop-color="#8d9299"/>
        <stop offset="1" stop-color="#4b5058"/>
      </linearGradient>
    </defs>
    <rect x="50" y="40" width="1100" height="481" rx="28" fill="url(#rightBlue)"/>
    <path d="M50,40 H493 L520,57 L467,106 L376,521 H78 Q50,521 50,493 Z" fill="url(#panelBlue)"/>
    <path d="M505,0 H1200 V57 H520 Z" fill="#ffffff"/>
    <path d="M473,139 H1150 V470 L1108,512 H380 Z" fill="url(#city)" role="img" aria-label="Toronto skyline photograph in greyscale"/>
    <path d="M480,57 H1122 Q1150,57 1150,85 V106 H467 Z" fill="var(--black)"/>
    <path d="M467,106 H1150 V138 H458 Z" fill="var(--sky)"/>
    <path d="M50,58 H365 L340,157 H50 Z" fill="#ffffff"/>
    <path d="M370,58 H403 L378,157 H345 Z" fill="var(--sky)"/>
    <path d="M240,323 H394 L351,487 H50" fill="none" stroke="var(--mid-blue)" stroke-width="1.5"/>
    <path d="M825,479 H1103 L1092,521 H825 Z" fill="var(--black)"/>
  </svg>

  <div class="abs brand">
    <div class="brand-dot"></div>
    <div class="brand-name">QPT</div>
  </div>

  <div class="abs headline">Enabling Solutions for a Connected World</div>
  <div class="abs subline">We Distribute Products and Solution for Digital Infrastructure</div>

  <div class="abs unique">
    <h2>What Makes us Unique?</h2>
    <p><b>QPT Touch:</b> We are more than a catalog</p>
    <p><b>QPT Experience:</b> A pleasure to do business with Proactive, Professional and Precise</p>
    <p><b>QPT Solution:</b> Design, Develop, and Deliver Custom Solution; On-Time and on-Spec</p>
  </div>

  <div class="abs values-title">Our Core Values</div>

  <div class="pill" style="left:75px;top:348px;width:132px">
    <div class="pill-icon"><svg width="20" height="16" viewBox="0 0 20 16" fill="none" stroke="#0054aa" stroke-width="1.6"><circle cx="10" cy="5" r="2.6"/><circle cx="4" cy="6" r="2"/><circle cx="16" cy="6" r="2"/><path d="M5,15 Q10,8 15,15M0.8,14 Q3,9.5 6.5,11M19.2,14 Q17,9.5 13.5,11"/></svg></div>
    <div class="pill-label">People First</div>
  </div>
  <div class="pill" style="left:220px;top:348px;width:136px">
    <div class="pill-icon"><svg width="18" height="18" viewBox="0 0 18 18" fill="none" stroke="#0054aa" stroke-width="1.6"><path d="M3,9 A6,6 0 1 1 9,15"/><path d="M3,5 V9 H7"/><path d="M7,12 V10M10,12 V8M13,12 V6"/></svg></div>
    <div class="pill-label">Continuous<br>Improvement</div>
  </div>
  <div class="pill" style="left:75px;top:394px;width:132px">
    <div class="pill-icon"><svg width="18" height="18" viewBox="0 0 18 18" fill="none" stroke="#0054aa" stroke-width="1.6"><path d="M5,16 V12 Q2,10 3,6 Q5,1 10,2 Q15,3 15,8 L16,11 H14 V14 H10 V16"/><circle cx="9" cy="7" r="2.2"/></svg></div>
    <div class="pill-label">Intellectual<br>Curiosity</div>
  </div>
  <div class="pill" style="left:220px;top:394px;width:136px">
    <div class="pill-icon"><svg width="18" height="18" viewBox="0 0 18 18" fill="none" stroke="#0054aa" stroke-width="1.6"><circle cx="9" cy="9" r="7"/><circle cx="9" cy="9" r="4"/><circle cx="9" cy="9" r="1.2" fill="#0054aa"/><path d="M9,9 L16,2"/></svg></div>
    <div class="pill-label">Customer<br>Focus</div>
  </div>
  <div class="pill" style="left:75px;top:443px;width:135px">
    <div class="pill-icon"><svg width="18" height="18" viewBox="0 0 18 18" fill="none" stroke="#0054aa" stroke-width="1.6"><path d="M4,16 V9 H7 L9,4 Q11,4 10.5,8 H15 L13.5,16 Z"/><path d="M3,4 L4,3M9,1 V2M14,3 L15,2"/></svg></div>
    <div class="pill-label">Results Matter</div>
  </div>

  <div class="card" style="left:526px;top:178px;width:154px;height:226px">
    <svg class="card-tab" viewBox="0 0 108 33" aria-hidden="true"><path d="M6,0 H102 L108,10 V33 H0 V10 Z" fill="#0b2f6b"/></svg>
    <div class="card-tab"><span>Our<br>Capabilities</span></div>
    <div class="card-frame">
      <ul>
        <li>Wireless Infrastructure</li>
        <li>Broadband &amp; Fiber</li>
        <li>Site Solutions</li>
        <li>Fixed Wireless Access</li>
        <li>Test &amp; Measurement</li>
        <li>DAS &amp; PWN</li>
        <li>Power Solutions</li>
      </ul>
      <div class="card-photo" role="img" aria-label="Photo of technicians working on a telecom tower" style="height:76px;background:linear-gradient(180deg,#a9b4c2,#6d7a68)"></div>
    </div>
  </div>

  <div class="card" style="left:726px;top:178px;width:154px;height:226px">
    <svg class="card-tab" viewBox="0 0 108 33" aria-hidden="true"><path d="M6,0 H102 L108,10 V33 H0 V10 Z" fill="#0b2f6b"/></svg>
    <div class="card-tab"><span>Solutions<br>Services</span></div>
    <div class="card-frame">
      <ul>
        <li>Kitting &amp; Logistics</li>
        <li>Professional<br>Engineering</li>
        <li>Lorem Ipsum 3</li>
        <li>Lorem Ipsum 4</li>
        <li>Lorem Ipsum 5</li>
        <li>Lorem Ipsum 6</li>
      </ul>
      <div class="card-photo" role="img" aria-label="Photo of a warehouse worker among stacked boxes" style="height:76px;background:linear-gradient(180deg,#5a5e66,#8b6a45)"></div>
    </div>
  </div>

  <div class="card" style="left:926px;top:178px;width:154px;height:245px">
    <svg class="card-tab" viewBox="0 0 108 33" aria-hidden="true"><path d="M6,0 H102 L108,10 V33 H0 V10 Z" fill="#0b2f6b"/></svg>
    <div class="card-tab"><span>Our<br>Markets</span></div>
    <div class="card-frame">
      <ul>
        <li>Carriers &amp; Cable<br>Companies</li>
        <li>Data Centers</li>
        <li>Utilities</li>
        <li>Federal Government</li>
        <li>Education</li>
        <li>Industrial<br>Manufacturing &amp;<br>Digital Supply Chain</li>
      </ul>
      <div class="card-photo" role="img" aria-label="Photo of a technician testing network cables in a server rack" style="height:70px;background:linear-gradient(135deg,#3a4a7a,#1c2550 60%,#b8502a)"></div>
    </div>
  </div>

  <div class="abs url">www.qalverpoint.com</div>
</div>
</body>
</html>
```